Business card for massage therapy company called Brook Fern Wellness

Need business card for massage therapy company called Brook Fern Wellness. Would like my logo on the front and the back of the card I have 3 options of logos and you can play with what looks better.

Would like this information displayed on the back of the card:

Marcus Ellery
Licensed Massage Therapist
321-555-0147
brookfern-example.com
brookfern_rest_

```html
<!DOCTYPE html>
<html lang="en">
<head>
<meta charset="utf-8">
<title>Brook Fern Wellness – Business Card</title>
<link rel="stylesheet" href="https://fonts.googleapis.com/css2?family=Montserrat:wght@300;400;500&family=Mrs+Saint+Delafield&display=swap">
<style>
  :root {
    --backdrop: #d6d6d6;
    --sage: #737a63;
    --sage-ink: #6c7060;
    --clay: #c09571;
    --clay-ink: #c49a76;
    --ink: #1d1b1a;
    --paper: #ffffff;
    --leaf-ghost: #f3f3f2;
    --shadow: rgba(0, 0, 0, 0.45);
  }
  * { box-sizing: border-box; margin: 0; padding: 0; }
  html, body {
    width: 1200px;
    height: 1200px;
    overflow: hidden;
    background: var(--backdrop);
  }
  .canvas {
    position: relative;
    width: 1200px;
    height: 1200px;
    background: var(--backdrop);
  }
  .card {
    position: absolute;
    left: 150px;
    width: 900px;
    height: 514px;
    overflow: hidden;
    box-shadow: 12px 14px 14px var(--shadow);
  }
  .card--front { top: 70px; display: flex; }
  .card--back { top: 616px; background: var(--paper); }

  /* Front: sage brand panel */
  .brand-panel {
    position: relative;
    width: 437px;
    height: 100%;
    background: var(--sage);
  }
  .brand-badge {
    position: absolute;
    left: 92px;
    top: 123px;
    width: 258px;
    height: 258px;
    border: 3px solid var(--paper);
    border-radius: 50%;
    display: flex;
    align-items: center;
    justify-content: center;
    text-align: center;
  }
  .brand-badge__name {
    font-family: "Montserrat", sans-serif;
    font-weight: 400;
    font-size: 25px;
    line-height: 1.35;
    letter-spacing: 0.12em;
    text-transform: uppercase;
    color: var(--paper);
  }

  /* Front: clay contact panel */
  .contact-panel {
    position: relative;
    flex: 1;
    height: 100%;
    background: var(--clay);
    color: var(--ink);
  }
  .person-name {
    position: absolute;
    left: 44px;
    top: 78px;
    font-family: "Mrs Saint Delafield", cursive;
    font-weight: 400;
    font-size: 92px;
    line-height: 1;
    white-space: nowrap;
  }
  .person-title {
    position: absolute;
    left: 48px;
    top: 196px;
    font-family: "Montserrat", sans-serif;
    font-weight: 400;
    font-size: 23px;
    letter-spacing: 0.01em;
    white-space: nowrap;
  }
  .contact-list {
    position: absolute;
    right: 28px;
    top: 318px;
    list-style: none;
    font-family: "Montserrat", sans-serif;
    font-weight: 400;
    font-size: 23px;
    letter-spacing: 0.01em;
  }
  .contact-list__item {
    display: flex;
    align-items: center;
    justify-content: flex-end;
    gap: 14px;
    height: 36px;
  }
  .contact-list__icon {
    width: 20px;
    height: 20px;
    flex: none;
  }

  /* Back */
  .wordmark {
    position: absolute;
    left: 92px;
    top: 212px;
    text-align: center;
    font-family: "Montserrat", sans-serif;
    font-weight: 400;
    color: var(--sage-ink);
  }
  .wordmark__name {
    font-size: 46px;
    line-height: 1.15;
    letter-spacing: 0.04em;
  }
  .leaf-motif {
    position: absolute;
    left: 566px;
    top: 18px;
    width: 290px;
    height: 496px;
    border-radius: 60% 40% 20% 50% / 45% 40% 30% 40%;
    background: linear-gradient(160deg, var(--leaf-ghost) 0%, #f6f6f5 60%, var(--paper) 100%);
  }
</style>
</head>
<body>
<main class="canvas">

  <section class="card card--front" aria-label="Business card front">
    <div class="brand-panel">
      <div class="brand-badge">
        <span class="brand-badge__name">Brook Fern<br>Wellness</span>
      </div>
    </div>

    <div class="contact-panel">
      <h1 class="person-name">Marcus Ellery</h1>
      <p class="person-title">Licensed Massage Therapist</p>

      <ul class="contact-list">
        <li class="contact-list__item">
          <span>321-555-0147</span>
          <svg class="contact-list__icon" viewBox="0 0 24 24" aria-hidden="true">
            <path d="M6.6 3.5l3 3.2-1.8 2.2c1.2 2.6 3.1 4.6 5.6 5.9l2.2-1.8 3.2 3-1.6 3.2c-6.8-.6-12.5-6.4-13.1-13.1z" fill="none" stroke="#1d1b1a" stroke-width="2" stroke-linejoin="round"/>
            <path d="M14.5 3.5a6 6 0 0 1 6 6M14.5 7a2.6 2.6 0 0 1 2.6 2.6" fill="none" stroke="#1d1b1a" stroke-width="1.8" stroke-linecap="round"/>
          </svg>
        </li>
        <li class="contact-list__item">
          <span>brookfern-example.com</span>
          <svg class="contact-list__icon" viewBox="0 0 24 24" aria-hidden="true">
            <circle cx="12" cy="12" r="9" fill="none" stroke="#1d1b1a" stroke-width="2"/>
            <ellipse cx="12" cy="12" rx="4" ry="9" fill="none" stroke="#1d1b1a" stroke-width="1.6"/>
            <path d="M3.5 9h17M3.5 15h17" stroke="#1d1b1a" stroke-width="1.6"/>
          </svg>
        </li>
        <li class="contact-list__item">
          <span>brookfern_rest_</span>
          <svg class="contact-list__icon" viewBox="0 0 24 24" aria-hidden="true">
            <rect x="4" y="4" width="16" height="16" rx="3" fill="none" stroke="#1d1b1a" stroke-width="2"/>
          </svg>
        </li>
      </ul>
    </div>
  </section>

  <section class="card card--back" aria-label="Business card back">
    <div class="leaf-motif" role="img" aria-label="Faint oversized leaf sprig decoration"></div>
    <div class="wordmark">
      <p class="wordmark__name">Brook Fern Wellness</p>
    </div>
  </section>

</main>
</body>
</html>
```